Brindle Capital and Investments

Create a simple business card design using the logos attached. Make it similar but not exact to the reference photo. Brand guidelines are also included.

```html
<!DOCTYPE html>
<html lang="en">
<head>
<meta charset="utf-8">
<title>Brindle Capital – Business Card</title>
<link rel="stylesheet" href="https://fonts.googleapis.com/css2?family=Arimo:wght@400;700&display=swap">
<style>
  :root {
    --backdrop: #5b5b5b;
    --navy: #000b3a;
    --copper: #9a4a12;
    --paper: #ffffff;
  }
  * { margin: 0; padding: 0; box-sizing: border-box; }
  html, body {
    width: 1200px; height: 1200px; overflow: hidden;
    background: var(--backdrop);
    font-family: "Arimo", Arial, sans-serif;
  }
  .card {
    position: absolute;
    width: 690px; height: 394px;
    overflow: hidden;
  }
  .card--front { left: 266px; top: 158px; background: var(--paper); }
  .card--back { left: 260px; top: 651px; background: var(--navy); }

  .card__wave { position: absolute; inset: 0; width: 100%; height: 100%; }

  .brand {
    position: absolute; left: 49px; top: 40px; width: 214px; height: 175px;
    display: flex; flex-direction: column; align-items: center; justify-content: center; gap: 18px;
  }
  .brand__dot {
    width: 58px; height: 58px; border-radius: 50%; background: var(--copper);
  }
  .brand__name {
    font-weight: 700; font-size: 27px; letter-spacing: 2px;
    color: var(--navy); text-transform: uppercase; white-space: nowrap;
  }

  .person { position: absolute; right: 37px; top: 64px; text-align: right; }
  .person__name { font-weight: 700; font-size: 26px; color: var(--navy); letter-spacing: 0.3px; }
  .person__role { font-size: 15px; color: var(--copper); margin-top: 4px; }

  .address {
    position: absolute; left: 49px; top: 318px;
    color: var(--paper); font-size: 16px; line-height: 21px;
  }
  .contacts {
    position: absolute; right: 37px; top: 278px;
    list-style: none; color: var(--paper); font-size: 16px;
  }
  .contacts li {
    display: flex; align-items: center; justify-content: flex-end;
    height: 21px; gap: 10px;
  }
  .contacts svg { width: 14px; height: 14px; fill: var(--copper); flex: none; }

  .back-brand {
    position: absolute; left: 0; right: 0; top: 110px;
    display: flex; flex-direction: column; align-items: center; gap: 22px;
  }
  .back-brand__dot { width: 70px; height: 70px; border-radius: 50%; background: var(--copper); }
  .back-brand__name {
    font-weight: 700; font-size: 40px; letter-spacing: 3px;
    color: var(--paper); text-transform: uppercase;
  }
  .back-url {
    position: absolute; left: 0; right: 0; top: 336px;
    text-align: center; color: var(--paper); font-size: 16px;
  }
</style>
</head>
<body>

<section class="card card--front">
  <svg class="card__wave" viewBox="0 0 1108 633" preserveAspectRatio="none" aria-hidden="true">
    <path fill="var(--navy)" d="M0,400 C150,470 300,450 500,410 C700,370 900,300 1030,335 C1080,350 1100,380 1108,395 L1108,633 L0,633 Z"/>
    <path fill="var(--copper)" d="M10,410 C150,475 320,458 520,418 C720,378 900,322 1010,340 C1060,350 1090,370 1100,387 C1080,374 1050,355 1000,350 C880,338 720,392 520,436 C320,474 150,476 10,410 Z"/>
  </svg>

  <div class="brand">
    <span class="brand__dot"></span>
    <span class="brand__name">Brindle Capital</span>
  </div>

  <div class="person">
    <p class="person__name">AVERY HOLT</p>
    <p class="person__role">President</p>
  </div>

  <address class="address" style="font-style:normal">
    4120 Juniper Row<br>Halden, Canada 58211
  </address>

  <ul class="contacts">
    <li>415-290-7713
      <svg viewBox="0 0 24 24"><path d="M6.6 10.8a15.1 15.1 0 0 0 6.6 6.6l2.2-2.2a1 1 0 0 1 1-.25 11.4 11.4 0 0 0 3.6.57 1 1 0 0 1 1 1V20a1 1 0 0 1-1 1A17 17 0 0 1 3 4a1 1 0 0 1 1-1h3.5a1 1 0 0 1 1 1c0 1.25.2 2.45.57 3.57a1 1 0 0 1-.25 1z"/></svg>
    </li>
    <li>415-388-2046
      <svg viewBox="0 0 24 24"><path d="M7 1h10a2 2 0 0 1 2 2v18a2 2 0 0 1-2 2H7a2 2 0 0 1-2-2V3a2 2 0 0 1 2-2zm0 3v15h10V4z"/></svg>
    </li>
    <li>info@brindlecapital.com
      <svg viewBox="0 0 24 24"><path d="M2 5h20v14H2zm2 2v.4l8 5 8-5V7zm0 2.8V17h16V9.8l-8 5z"/></svg>
    </li>
    <li>www.brindlecapital.com
      <svg viewBox="0 0 24 24"><path d="M12 2a10 10 0 1 0 0 20 10 10 0 0 0 0-20zm-1 17.9A8 8 0 0 1 4.2 10L9 14.8v1a2 2 0 0 0 2 2zm6.9-2.5A2 2 0 0 0 16 16h-1v-3a1 1 0 0 0-1-1H8v-2h2a1 1 0 0 0 1-1V7h2a2 2 0 0 0 2-2v-.4a8 8 0 0 1 2.9 12.8z"/></svg>
    </li>
  </ul>
</section>

<section class="card card--back">
  <div class="back-brand">
    <span class="back-brand__dot"></span>
    <span class="back-brand__name">Brindle Capital</span>
  </div>
  <p class="back-url">www.brindlecapital.com</p>
</section>

</body>
</html>
```